Motivation Quotes Wall Art

Our public bathrooms are quite loud and we would like to put some sound deadening wall acoustical panels in there to quiet it down. I would like to create two 4' wide x 2' tall or 4' wide x 3' tall designs that will be put onto this acoustical wall panel. The art will be in the form of motivational quotes. One for the women's and one for the men's. I would like you to use different fonts color and background design but yet still be very simple.
I would like the first quote to be in the center of the womens's & men's board.
1. You are amazing, remember that
2. It doesn't make sense to hire smart people and then tell them what to do; we hire smart people so they can tell us what to do.
3. The chains of habit are to light to be felt until they are to heavy to be broken.  
4. My boss said I intimidate coworkers.    I stared at him until he apologized.
5. Every job is a self-portrait of the person who did it.  Autograph your work with excellence.
6. A wise man can learn more from a foolish question than a fool can learn from a wise answer.
7. Today you are YOU.  that is TRUER that true. there is NO ONE alive who is YOUER than YOU!
8. Success is the sum of small efforts, repeated day in and day out
9. Happiness is a way of travel, not a destination
10. Don't look back you're not going that way
11. Be yourself, everyone else is already taken
12. The pessimist sees difficulty in every opportunity.  The optimist sees the opportunity in every difficulty.
13. Integrity, the choice between what's convenient and what's right
14. Success without integrity is failure
15. You don't choose your passions.  Your passions choose you.
16. Most great people have attained their greatest success just one step beyond their greatest failure.
17. If you cannot do great things, do small things in a great way.
18. Things work out best for those who make the best of how things work out.
19. Making mistakes is better than faking perfections.
20. Alone we can do so little; together we can do so much

```html
<!DOCTYPE html>
<html lang="en">
<head>
<meta charset="utf-8">
<title>Motivation Quotes Wall Art</title>
<link rel="stylesheet" href="https://fonts.googleapis.com/css2?family=Kalam:wght@700&family=Dancing+Script:wght@500&family=Pacifico&family=Great+Vibes&family=Alfa+Slab+One&family=Anton&family=Lilita+One&family=Montserrat:wght@300;500;700&family=Caveat+Brush&family=Kaushan+Script&family=Archivo+Black&display=swap">
<style>
  :root{
    --ink:#111111;
    --white:#ffffff;
    --paper:#f4f4f4;
    --night:#0d0d1f;
    --orange:#f07f3c;
    --violet:#6a3fb5;
    --lemon:#e8d52c;
    --teal:#1aa9a5;
    --leaf:#3d6b25;
    --leaf-soft:#cfe0c4;
    --leaf-deep:#1f3318;
    --crimson:#c62828;
    --gold:#f0b03a;
    --ember:#e8692e;
    --coral:#ee5253;
    --sun:#fbc318;
    --amber:#f0ae17;
    --charcoal:#3d3d3d;
    --sea:#64a9a6;
    --sea-deep:#5b9c99;
    --quote-mark:#3c6f73;
  }
  *{margin:0;padding:0;box-sizing:border-box}
  html,body{width:1200px;height:900px;overflow:hidden;background:var(--white)}
  .wall{display:grid;grid-template-columns:repeat(3,400px);grid-template-rows:repeat(3,300px);width:1200px;height:900px}
  .tile{width:400px;height:300px;display:block}
  .tile svg{width:400px;height:300px;display:block}
  .wise-quote .bold{font-family:"Kalam",cursive;font-weight:700;font-size:28px;fill:var(--ink)}
  .wise-quote .script{font-family:"Dancing Script",cursive;font-size:30px;fill:var(--ink)}
  .together .big{font-family:"Pacifico",cursive}
  .together .small{font-family:"Montserrat",sans-serif;font-weight:500}
  .portrait .arc{font-family:"Montserrat",sans-serif;font-weight:700;font-size:13px;letter-spacing:3px;fill:var(--ink)}
  .portrait .script{font-family:"Great Vibes",cursive;fill:var(--ink)}
  .portrait .autograph{fill:var(--crimson)}
  .portrait .slab{font-family:"Alfa Slab One",serif;fill:var(--ink)}
  .be-yourself text{font-family:"Anton",sans-serif}
  .be-yourself .is{font-family:"Pacifico",cursive}
  .amazing .heavy{font-family:"Lilita One",sans-serif;fill:var(--white)}
  .amazing .thin{font-family:"Montserrat",sans-serif;font-weight:300;fill:var(--white)}
  .success .line{font-family:"Archivo Black",sans-serif;font-size:25px;fill:var(--ink)}
  .success .brace{font-family:"Montserrat",sans-serif;font-weight:300;fill:var(--ink)}
  .look-back text{font-family:"Caveat Brush",cursive}
  .optimist .caption{font-family:"Montserrat",sans-serif;font-weight:700;font-size:9.2px;fill:var(--white)}
  .optimist .mark{font-family:"Archivo Black",sans-serif;font-size:46px;fill:var(--quote-mark)}
  .mistakes .sans{font-family:"Montserrat",sans-serif;font-weight:500;fill:var(--ink)}
  .mistakes .script{font-family:"Kaushan Script",cursive;fill:var(--ink)}
</style>
</head>
<body>
<main class="wall">

  <section class="tile wise-quote">
    <svg viewBox="0 0 400 300">
      <rect width="400" height="300" fill="var(--white)"/>
      <line x1="80" y1="55" x2="322" y2="55" stroke="var(--ink)" stroke-width="1.5"/>
      <text class="bold" x="201" y="97" text-anchor="middle" textLength="245" lengthAdjust="spacingAndGlyphs">A wise man can learn more</text>
      <text class="script" x="201" y="134" text-anchor="middle" textLength="245" lengthAdjust="spacingAndGlyphs">from a foolish question</text>
      <text class="bold" x="201" y="181" text-anchor="middle" textLength="245" lengthAdjust="spacingAndGlyphs">than a fool can learn</text>
      <text class="script" x="201" y="218" text-anchor="middle" textLength="245" lengthAdjust="spacingAndGlyphs">from a wise answer</text>
      <line x1="80" y1="248" x2="322" y2="248" stroke="var(--ink)" stroke-width="1.5"/>
    </svg>
  </section>

  <section class="tile together">
    <svg viewBox="0 0 400 300">
      <rect width="400" height="300" fill="#000"/>
      <rect role="img" aria-label="Laurel wreath, left branch" x="42" y="50" width="48" height="210" rx="24" fill="var(--leaf-deep)"/>
      <rect role="img" aria-label="Laurel wreath, right branch" x="310" y="50" width="48" height="210" rx="24" fill="var(--leaf-deep)"/>
      <text class="big" x="205" y="108" text-anchor="middle" font-size="62" fill="var(--orange)">alone</text>
      <text class="small" x="112" y="130" font-size="11" fill="var(--violet)">WE CAN DO SO</text>
      <text class="small" x="133" y="148" font-size="17" fill="var(--lemon)">LITTLE</text>
      <text class="big" x="210" y="205" text-anchor="middle" font-size="66" fill="var(--teal)">together</text>
      <text class="small" x="202" y="217" font-size="11" fill="var(--violet)">WE CAN DO</text>
      <text class="small" x="201" y="236" font-size="17" fill="#e53a2c">SO MUCH</text>
    </svg>
  </section>

  <section class="tile portrait">
    <svg viewBox="0 0 400 300">
      <defs>
        <path id="arcTop" d="M90 85 Q200 45 310 85"/>
        <path id="arcBottom" d="M60 212 Q200 268 345 205"/>
      </defs>
      <rect width="400" height="300" fill="var(--white)"/>
      <text class="arc"><textPath href="#arcTop" startOffset="50%" text-anchor="middle">EVERY JOB IS A</textPath></text>
      <text class="script" x="200" y="128" text-anchor="middle" font-size="72" textLength="390" lengthAdjust="spacingAndGlyphs">Self Potrait</text>
      <text class="slab" x="200" y="162" text-anchor="middle" font-size="25" letter-spacing="1">OF THE PERSON</text>
      <line x1="102" y1="180" x2="118" y2="180" stroke="var(--ink)" stroke-width="1.5"/>
      <text class="script" x="200" y="186" text-anchor="middle" font-size="28" font-weight="700">who does it</text>
      <line x1="282" y1="180" x2="298" y2="180" stroke="var(--ink)" stroke-width="1.5"/>
      <text class="script autograph" x="200" y="212" text-anchor="middle" font-size="32">Autograph</text>
      <text class="arc"><textPath href="#arcBottom" startOffset="50%" text-anchor="middle">YOUR WORK WITH EXCELLENCE</textPath></text>
    </svg>
  </section>

  <section class="tile be-yourself">
    <svg viewBox="0 0 400 300">
      <rect width="400" height="300" fill="var(--night)"/>
      <g stroke="var(--white)" stroke-width="3" stroke-dasharray="1 9" stroke-linecap="round">
        <line x1="26" y1="80" x2="26" y2="275"/><line x1="195" y1="80" x2="195" y2="275"/>
        <line x1="216" y1="80" x2="216" y2="275"/><line x1="386" y1="80" x2="386" y2="275"/>
      </g>
      <g fill="none" stroke="var(--white)" stroke-width="2">
        <path d="M96 52 L96 38 L104 46 L111 36 L118 46 L126 38 L126 52 Z"/>
        <path d="M287 52 L287 38 L295 46 L302 36 L309 46 L317 38 L317 52 Z"/>
        <path d="M35 72 H62 M52 64 L62 72 L52 80 M187 72 H160 M170 64 L160 72 L170 80"/>
        <path d="M226 72 H253 M243 64 L253 72 L243 80 M378 72 H351 M361 64 L351 72 L361 80"/>
        <path d="M55 192 H82 M72 184 L82 192 L72 200 M167 192 H140 M150 184 L140 192 L150 200"/>
        <path d="M246 192 H273 M263 184 L273 192 L263 200 M358 192 H331 M341 184 L331 192 L341 200"/>
      </g>
      <g text-anchor="middle" lengthAdjust="spacingAndGlyphs">
        <text x="111" y="85" font-size="34" textLength="58" lengthAdjust="spacingAndGlyphs" fill="var(--gold)">BE</text>
        <text x="111" y="116" font-size="30" textLength="130" lengthAdjust="spacingAndGlyphs" fill="var(--ember)">YOURSELF</text>
        <text x="111" y="143" font-size="28" textLength="130" lengthAdjust="spacingAndGlyphs" fill="var(--white)">EVERYONE</text>
        <text x="111" y="173" font-size="32" textLength="128" lengthAdjust="spacingAndGlyphs" fill="var(--gold)">ELSE</text>
        <text class="is" x="111" y="203" font-size="24" fill="var(--white)">is</text>
        <text x="111" y="240" font-size="33" textLength="128" lengthAdjust="spacingAndGlyphs" fill="var(--ember)">ALREADY</text>
        <text x="111" y="272" font-size="34" textLength="135" lengthAdjust="spacingAndGlyphs" fill="var(--gold)">TAKEN</text>
        <text x="302" y="85" font-size="34" textLength="58" lengthAdjust="spacingAndGlyphs" fill="var(--white)">BE</text>
        <text x="302" y="116" font-size="30" textLength="130" lengthAdjust="spacingAndGlyphs" fill="var(--white)">YOURSELF</text>
        <text x="302" y="143" font-size="28" textLength="130" lengthAdjust="spacingAndGlyphs" fill="var(--white)">EVERYONE</text>
        <text x="302" y="173" font-size="32" textLength="128" lengthAdjust="spacingAndGlyphs" fill="var(--white)">ELSE</text>
        <text class="is" x="302" y="203" font-size="24" fill="var(--white)">is</text>
        <text x="302" y="240" font-size="33" textLength="128" lengthAdjust="spacingAndGlyphs" fill="var(--white)">ALREADY</text>
        <text x="302" y="272" font-size="34" textLength="135" lengthAdjust="spacingAndGlyphs" fill="var(--white)">TAKEN</text>
      </g>
    </svg>
  </section>

  <section class="tile amazing">
    <svg viewBox="0 0 400 300">
      <rect width="400" height="300" fill="var(--white)"/>
      <g fill="none" stroke="var(--ink)" stroke-width="1.2">
        <circle cx="122" cy="13" r="7"/><circle cx="30" cy="238" r="7"/><circle cx="252" cy="296" r="6"/>
        <path d="M73 35 L68 48 M62 60 L58 72 M52 85 L50 95"/>
        <path d="M350 240 L338 246 M330 250 L318 256 M310 260 L300 264"/>
        <path d="M358 31 V41 M353 36 H363 M145 295 V305 M140 300 H150"/>
      </g>
      <rect x="87" y="56" width="245" height="214" rx="32" fill="none" stroke="var(--ink)" stroke-width="3"/>
      <path d="M98 58 Q100 50 130 48 L305 46 Q325 46 330 70 L338 240 Q336 262 310 265 L120 272 Q95 272 93 248 Z" fill="var(--coral)"/>
      <text class="heavy" x="205" y="115" text-anchor="middle" font-size="38">YOU ARE</text>
      <text class="thin" x="205" y="152" text-anchor="middle" font-size="34" letter-spacing="1">AMAZING</text>
      <text class="heavy" x="205" y="185" text-anchor="middle" font-size="28">REMEMBER</text>
      <text class="heavy" x="205" y="238" text-anchor="middle" font-size="60">THAT</text>
    </svg>
  </section>

  <section class="tile success">
    <svg viewBox="0 0 400 300">
      <rect width="400" height="300" fill="var(--sun)"/>
      <path d="M60 35 Q200 20 345 38 L352 270 Q200 282 55 268 Z" fill="var(--white)"/>
      <text class="brace" x="18" y="235" font-size="210">{</text>
      <text class="brace" x="318" y="235" font-size="210">}</text>
      <g text-anchor="middle">
        <text class="line" x="200" y="70">SUCCESS</text>
        <text class="line" x="200" y="93">IS THE SUM</text>
        <text class="line" x="200" y="116">OF SMALL</text>
        <text class="line" x="200" y="139">EFFORTS,</text>
        <text class="line" x="200" y="162">REPEATED</text>
        <text class="line" x="200" y="185">DAY IN</text>
        <text class="line" x="200" y="208">&amp; DAY OUT.</text>
      </g>
    </svg>
  </section>

  <section class="tile look-back">
    <svg viewBox="0 0 400 300">
      <rect width="400" height="300" fill="var(--amber)"/>
      <path d="M110 55 Q200 42 285 52 Q302 56 300 80 L298 245 Q296 265 275 266 L125 268 Q100 268 98 245 L95 80 Q96 57 110 55 Z" fill="var(--charcoal)"/>
      <text x="133" y="118" font-size="34" fill="var(--gold)">don't look</text>
      <text x="145" y="168" font-size="56" fill="var(--white)">back</text>
      <text x="155" y="196" font-size="26" fill="var(--gold)">- you're</text>
      <text x="125" y="226" font-size="34" fill="var(--white)">not <tspan fill="var(--gold)">going</tspan></text>
      <text x="147" y="258" font-size="34" fill="var(--gold)">that <tspan fill="var(--white)">way.</tspan></text>
    </svg>
  </section>

  <section class="tile optimist">
    <svg viewBox="0 0 400 300">
      <defs>
        <linearGradient id="sceneTone" x1="0" y1="0" x2="0" y2="1">
          <stop offset="0" stop-color="var(--sea)"/>
          <stop offset="1" stop-color="var(--sea-deep)"/>
        </linearGradient>
      </defs>
      <rect width="400" height="300" fill="var(--sea)"/>
      <line x1="12" y1="12" x2="388" y2="12" stroke="var(--white)" stroke-width="1"/>
      <line x1="12" y1="55" x2="388" y2="55" stroke="var(--white)" stroke-width="1"/>
      <text class="mark" x="10" y="60">“</text>
      <text class="mark" x="348" y="60">”</text>
      <text class="caption" x="200" y="30" text-anchor="middle">The Pessimist Sees Difficulty In Every Opportunity.</text>
      <text class="caption" x="200" y="41" text-anchor="middle">The Optimist Sees Opportunity In Every Difficulty.</text>
      <rect role="img" aria-label="Illustration of a climber reaching a trophy and flag on a mountain peak while another person watches from below" x="0" y="64" width="400" height="236" fill="url(#sceneTone)"/>
    </svg>
  </section>

  <section class="tile mistakes">
    <svg viewBox="0 0 400 300">
      <rect width="400" height="300" fill="var(--paper)"/>
      <rect role="img" aria-label="Floral ornament of red roses and leaves, top left" x="10" y="14" width="120" height="120" rx="20" fill="var(--leaf-soft)"/>
      <rect role="img" aria-label="Floral ornament of red roses and leaves, bottom right" x="270" y="166" width="120" height="124" rx="20" fill="var(--leaf-soft)"/>
      <ellipse cx="200" cy="190" rx="150" ry="80" fill="#d9d9d9"/>
      <text class="sans" x="200" y="60" text-anchor="middle" font-size="17">MAKING</text>
      <text class="script" x="200" y="118" text-anchor="middle" font-size="58">mistakes</text>
      <text class="sans" x="200" y="144" text-anchor="middle" font-size="16">IS BETTER THAN</text>
      <text class="sans" x="200" y="162" text-anchor="middle" font-size="16">FAKING</text>
      <text class="script" x="200" y="222" text-anchor="middle" font-size="62">Perfection</text>
    </svg>
  </section>

</main>
</body>
</html>
```